Business Card Design Project

Business card design with a funky, clean, modern design. Business is an immigration consultancy. Client base will be Canadian employers wanting to hire or retain foreign workers and foreign nationals wanting to immigrate to Canada.

Full color possible, but should incorporate red/white/black as per the logo to be provided. Double sided card design.

Target Market(s)

Canadian employers looking to hire/retain staff and also foreign nationals immigrating to Canada

Industry/Entity Type

Business

Requirements
Must have
• Logo (to be provided)
Name (Marla Voskuil, Immigration Consultant)
Phone (604) 731-5562
E-mail: marla@tallowbrookmigration.example
Web: www.tallowbrookmigration.example

Nice to have
• Tag Line
Clean, modern style

```html
<!DOCTYPE html>
<html lang="en">
<head>
<meta charset="utf-8">
<title>Tallowbrook Migration – Business Card</title>
<link rel="stylesheet" href="https://fonts.googleapis.com/css2?family=Source+Sans+3:wght@400;600;700&display=swap">
<style>
  :root {
    --backdrop: #c9d5dd;
    --brand-red: #b01f27;
    --brand-red-dark: #8a1a1f;
    --ink: #1c1c1c;
    --ink-soft: #3a3a3a;
    --paper: #ffffff;
  }
  * { margin: 0; padding: 0; box-sizing: border-box; }
  html, body { width: 1200px; height: 965px; overflow: hidden; }
  body {
    background: var(--backdrop);
    font-family: "Source Sans 3", Arial, sans-serif;
    position: relative;
  }
  .card {
    position: absolute;
    left: 284px;
    width: 630px;
    height: 359px;
    overflow: hidden;
  }
  .card--front {
    top: 101px;
    background: linear-gradient(180deg, var(--brand-red) 0%, var(--brand-red) 60%, var(--brand-red-dark) 100%);
  }
  .card--back {
    top: 517px;
    background: var(--paper);
  }
  .brand-mark {
    position: absolute;
    border-radius: 50%;
  }
  .card--front .brand-mark {
    width: 100px; height: 100px;
    left: 265px; top: 66px;
    background: var(--brand-red-dark);
  }
  .card--back .brand-mark {
    width: 110px; height: 110px;
    left: 96px; top: 36px;
    background: var(--brand-red);
  }
  .brand-name {
    position: absolute;
    font-weight: 700;
    color: var(--ink);
    text-transform: uppercase;
    text-align: center;
    line-height: 1.05;
    letter-spacing: 1px;
  }
  .card--front .brand-name {
    left: 0; right: 0; top: 184px;
    font-size: 27px;
  }
  .card--back .brand-name {
    left: 36px; width: 230px; top: 158px;
    font-size: 23px;
  }
  .web {
    position: absolute;
    left: 0; right: 0;
    text-align: center;
    font-size: 13px;
  }
  .card--front .web { top: 325px; color: var(--ink); }
  .card--back .web { top: 326px; color: var(--paper); }
  .holder { position: absolute; left: 59px; top: 216px; }
  .holder__name { font-size: 20px; font-weight: 700; color: var(--brand-red-dark); }
  .holder__title { font-size: 16px; color: var(--ink-soft); margin-top: 1px; }
  .contact {
    position: absolute;
    left: 376px; top: 172px;
    font-size: 13px;
    color: var(--ink);
    line-height: 1.35;
  }
  .contact__line { display: flex; align-items: center; gap: 8px; margin-top: 6px; }
  .contact__line svg { width: 15px; height: 15px; flex: none; }
  .footer-band { position: absolute; left: 0; bottom: 0; }
</style>
</head>
<body>
  <section class="card card--front">
    <span class="brand-mark"></span>
    <div class="brand-name">Tallowbrook<br>Migration</div>
    <div class="web">www.tallowbrookmigration.example</div>
  </section>

  <section class="card card--back">
    <span class="brand-mark"></span>
    <div class="brand-name">Tallowbrook<br>Migration</div>
    <div class="holder">
      <div class="holder__name">Marla Voskuil</div>
      <div class="holder__title">RCIC</div>
    </div>
    <div class="contact">
      <div>Offices in Alder Flats,<br>Cedarholm and Port Kessling</div>
      <div class="contact__line">
        <svg viewBox="0 0 16 16"><path fill="#8a1a1f" d="M3 1l3 3-1.5 2c1 2 2.5 3.5 4.5 4.5L11 9l3 3-2 2.5C6 14 2 10 1.5 3.5z"/></svg>
        <span>(604) 731-5562</span>
      </div>
      <div class="contact__line">
        <svg viewBox="0 0 16 16"><rect x="1" y="3.5" width="14" height="9" fill="#8a1a1f"/><path d="M1.5 4l6.5 5 6.5-5" fill="none" stroke="#fff" stroke-width="1.2"/></svg>
        <span>marla@tallowbrookmigration.example</span>
      </div>
    </div>
    <svg class="footer-band" width="630" height="50" viewBox="0 0 630 50">
      <path d="M25 50 C30 30 40 22 60 20 Q315 -6 570 20 C590 22 600 30 606 50 Z" fill="var(--brand-red)"/>
    </svg>
    <div class="web">www.tallowbrookmigration.example</div>
  </section>
</body>
</html>
```